Recreate a graphic of The Church Year

Take the uploaded graphic and recreate it (without the shield) for use by PWD, branding it with the PDW logo.

Target Market(s)

For use by PDW

Industry/Entity Type

Education

Font styles to use
Sans Serif

Requirements
Must have
• Use liturgical colors as in upload.
• The center of the circle must be empty except for the words The Church Year
• The PDW logo must be on the graphic
Nice to have
• None.

```html
<!DOCTYPE html>
<html lang="en">
<head>
<meta charset="utf-8">
<title>The Church Year – PDW</title>
<link rel="stylesheet" href="https://fonts.googleapis.com/css2?family=EB+Garamond:wght@400;500&display=swap">
<style>
  :root {
    --paper: #ffffff;
    --frame: #8a8a8a;
    --ink: #4a4a4a;
    --brand-blue: #1f86c2;
    --advent: #3b63c4;
    --christmas: #c9a64c;
    --epiphany: #16633a;
    --lent: #5a2379;
    --holy-week: #9a1b22;
    --easter: #c29a45;
    --ordinary: #218a48;
    --muted: #8c8c8c;
    --dot: #c0262d;
  }
  html, body {
    margin: 0;
    width: 1200px;
    height: 961px;
    overflow: hidden;
    background: var(--paper);
    font-family: "EB Garamond", Georgia, serif;
  }
  .poster {
    position: relative;
    width: 1200px;
    height: 961px;
  }
  .poster-frame {
    position: absolute;
    inset: 18px;
    border: 1.5px solid var(--frame);
  }
  .wordmark {
    position: absolute;
    top: 78px;
    left: 0;
    width: 1200px;
    text-align: center;
  }
  .wordmark-name {
    font-size: 44px;
    line-height: 1;
    color: var(--ink);
    font-weight: 400;
    letter-spacing: 8px;
  }
  .wordmark-tagline {
    margin-top: 10px;
    font-size: 16px;
    color: var(--muted);
    letter-spacing: 0.5px;
  }
  .calendar {
    position: absolute;
    left: 0;
    top: 0;
  }
  .ring-label { font-size: 15px; fill: #fff; }
  .feast { font-size: 12.5px; fill: var(--muted); }
  .season-name { font-size: 17px; fill: #fff; }
  .season-sub { font-size: 12px; fill: #fff; }
  .title { font-size: 48px; fill: var(--brand-blue); }
</style>
</head>
<body>
<main class="poster">
  <div class="poster-frame"></div>

  <header class="wordmark">
    <div class="wordmark-name">PDW</div>
    <div class="wordmark-tagline">learning · service · community</div>
  </header>

  <svg class="calendar" width="1200" height="961" viewBox="0 0 1200 961" aria-label="The Church Year liturgical calendar">
    <polygon class="accent-band" points="470,196 740,184 740,194 470,206" fill="var(--brand-blue)"/>

    <g class="season-ring" fill="none" stroke-width="55" transform="rotate(220 600 540)">
      <circle cx="600" cy="540" r="177.5" pathLength="360" stroke="var(--advent)" stroke-dasharray="35 360" stroke-dashoffset="0"/>
      <circle cx="600" cy="540" r="177.5" pathLength="360" stroke="var(--christmas)" stroke-dasharray="30 360" stroke-dashoffset="-35"/>
      <circle cx="600" cy="540" r="177.5" pathLength="360" stroke="var(--epiphany)" stroke-dasharray="45 360" stroke-dashoffset="-65"/>
      <circle cx="600" cy="540" r="177.5" pathLength="360" stroke="var(--lent)" stroke-dasharray="58 360" stroke-dashoffset="-110"/>
      <circle cx="600" cy="540" r="177.5" pathLength="360" stroke="var(--holy-week)" stroke-dasharray="7 360" stroke-dashoffset="-168"/>
      <circle cx="600" cy="540" r="177.5" pathLength="360" stroke="var(--easter)" stroke-dasharray="75 360" stroke-dashoffset="-175"/>
      <circle cx="600" cy="540" r="177.5" pathLength="360" stroke="var(--holy-week)" stroke-dasharray="2 360" stroke-dashoffset="-250"/>
      <circle cx="600" cy="540" r="177.5" pathLength="360" stroke="var(--epiphany)" stroke-dasharray="1 360" stroke-dashoffset="-252.3"/>
      <circle cx="600" cy="540" r="177.5" pathLength="360" stroke="var(--ordinary)" stroke-dasharray="106 360" stroke-dashoffset="-254"/>
      <circle cx="600" cy="540" r="177.5" pathLength="360" stroke="#ffffff" stroke-dasharray="0.6 360" stroke-dashoffset="-347.5"/>
    </g>

    <g class="ring-labels" text-anchor="middle" dominant-baseline="central">
      <text class="ring-label" transform="translate(506 390) rotate(-32)">4 Sundays</text>
      <text class="ring-label" transform="translate(600 363)">12 Days</text>
      <text class="ring-label" transform="translate(707 399) rotate(37)">4-8 Sundays</text>
      <text class="ring-label" transform="translate(777 528) rotate(86)">5 Sundays</text>
      <text class="ring-label" transform="translate(756 624) rotate(-61.5)">7 Days</text>
      <text class="ring-label" transform="translate(655 708) rotate(-18)">50 Days</text>
    </g>

    <g class="centre-title" text-anchor="middle">
      <text class="title" x="570" y="510">The</text>
      <text class="title" x="600" y="560">Church</text>
      <text class="title" x="630" y="610">Year</text>
    </g>

    <g class="feasts">
      <circle cx="411" cy="426" r="2.5" fill="var(--brand-blue)"/>
      <circle cx="409" cy="444" r="2.5" fill="var(--dot)"/>
      <circle cx="407" cy="462" r="2.5" fill="var(--dot)"/>
      <text class="feast" x="402" y="430" text-anchor="end">The Church Year Begins Here</text>
      <text class="feast" x="400" y="448" text-anchor="end">Christ the King Sunday</text>
      <text class="feast" x="398" y="466" text-anchor="end">All Saints Day</text>

      <circle cx="544" cy="330" r="2.5" fill="var(--dot)"/>
      <text class="feast" x="538" y="322" text-anchor="end">Birth of Our Lord (Christmas Eve, Christmas Day)</text>

      <circle cx="656" cy="330" r="2.5" fill="var(--dot)"/>
      <text class="feast" x="663" y="316">Day of Epiphany</text>
      <text class="feast" x="663" y="332">Baptism of Our Lord</text>

      <circle cx="786" cy="432" r="2.5" fill="var(--dot)"/>
      <text class="feast" x="794" y="422">Transfiguration</text>
      <text class="feast" x="794" y="438">Ash Wednesday</text>

      <circle cx="806" cy="600" r="2.5" fill="var(--dot)"/>
      <circle cx="804" cy="616" r="2.5" fill="var(--dot)"/>
      <circle cx="800" cy="632" r="2.5" fill="var(--dot)"/>
      <circle cx="796" cy="648" r="2.5" fill="var(--dot)"/>
      <text class="feast" x="814" y="604">Passion (Palm) Sunday</text>
      <text class="feast" x="812" y="620">Maundy Thursday</text>
      <text class="feast" x="808" y="636">The Passion of Our Lord (Good Friday)</text>
      <text class="feast" x="804" y="652">The Resurrection of Our Lord (Easter Sunday)</text>

      <circle cx="581" cy="758" r="2.5" fill="var(--dot)"/>
      <text class="feast" x="588" y="778">The Ascension of Our Lord</text>

      <circle cx="527" cy="764" r="2.5" fill="var(--dot)"/>
      <circle cx="527" cy="780" r="2.5" fill="var(--dot)"/>
      <text class="feast" x="520" y="768" text-anchor="end">Day of Pentecost</text>
      <text class="feast" x="520" y="784" text-anchor="end">Holy Trinity Sunday</text>
    </g>

    <g class="season-tags" text-anchor="middle" dominant-baseline="central">
      <rect x="262" y="350" width="160" height="36" rx="18" fill="var(--advent)"/>
      <text class="season-name" x="342" y="368">Advent Season</text>

      <rect x="468" y="232" width="164" height="36" rx="18" fill="var(--christmas)"/>
      <text class="season-name" x="550" y="250">Christmas Season</text>

      <rect x="706" y="262" width="164" height="36" rx="18" fill="var(--epiphany)"/>
      <text class="season-name" x="788" y="280">Epiphany Season</text>

      <rect x="850" y="350" width="150" height="36" rx="18" fill="var(--lent)"/>
      <text class="season-name" x="925" y="368">Season of Lent</text>

      <rect x="900" y="680" width="130" height="36" rx="18" fill="var(--holy-week)"/>
      <text class="season-name" x="965" y="698">Holy Week</text>

      <rect x="690" y="806" width="150" height="36" rx="18" fill="var(--easter)"/>
      <text class="season-name" x="765" y="824">Easter Season</text>

      <rect x="210" y="690" width="190" height="50" rx="25" fill="var(--ordinary)"/>
      <text class="season-name" x="305" y="707">Ordinary Time</text>
      <text class="season-sub" x="305" y="726">(Time after Pentecost)</text>
    </g>
  </svg>
</main>
</body>
</html>
```